Build Steady Practice Growth Through Trust

Design a cover for this book which is designed to help a business go from it's current revenue and treatment acceptance to double (2X) that success and those metrics.

```html
<!DOCTYPE html>
<html lang="en">
<head>
<meta charset="utf-8">
<title>Build Steady Practice Growth Through Trust – Book Cover</title>
<link rel="stylesheet" href="https://fonts.googleapis.com/css2?family=Oswald:wght@600;700&family=Montserrat:ital,wght@0,800;1,800&display=swap">
<style>
  :root {
    --page-bg: #e9e7e2;
    --navy-deep: #0b1a45;
    --navy-mid: #13306b;
    --blue-light: #2f6aa8;
    --gold-light: #f6e27a;
    --gold: #d9b43c;
    --gold-dark: #a8801e;
    --white: #ffffff;
  }
  * { margin: 0; padding: 0; box-sizing: border-box; }
  html, body {
    width: 1200px; height: 1200px; overflow: hidden;
    background: var(--page-bg);
  }
  .canvas {
    position: relative; width: 1200px; height: 1200px;
    display: flex; align-items: center; justify-content: center;
  }
  .book-cover {
    position: relative; width: 700px; height: 1080px; overflow: hidden;
    background:
      radial-gradient(ellipse at 85% 10%, var(--blue-light) 0%, rgba(47,106,168,0) 55%),
      linear-gradient(180deg, var(--navy-mid) 0%, var(--navy-deep) 70%);
    box-shadow: 0 20px 50px rgba(0,0,0,.25);
  }
  .cover-photo {
    position: absolute; left: 380px; top: 340px; width: 320px; height: 320px;
    background: radial-gradient(ellipse at 60% 45%, rgba(120,160,205,.30) 0%, rgba(40,80,140,.12) 50%, rgba(11,26,69,0) 75%);
  }
  .growth-graphic { position: absolute; left: 0; top: 0; width: 700px; height: 700px; }
  .title-block {
    position: absolute; left: 0; right: 0; top: 285px;
    text-align: center;
  }
  .title-lead, .title-accent {
    font-family: "Oswald", sans-serif; font-weight: 700;
    text-transform: uppercase; line-height: 1;
    background: linear-gradient(180deg, var(--gold-light) 0%, var(--gold) 55%, var(--gold-dark) 100%);
    -webkit-background-clip: text; background-clip: text; color: transparent;
  }
  .title-lead { font-size: 120px; letter-spacing: 1px; }
  .title-divider {
    display: flex; align-items: center; justify-content: center; gap: 18px;
    margin: 34px 0 12px;
  }
  .title-divider::before, .title-divider::after {
    content: ""; width: 150px; height: 2px; background: rgba(255,255,255,.55);
  }
  .title-connector {
    font-family: "Montserrat", sans-serif; font-style: italic; font-weight: 800;
    color: var(--white); font-size: 34px;
  }
  .title-main {
    font-family: "Oswald", sans-serif; font-weight: 700; text-transform: uppercase;
    color: var(--white); font-size: 80px; line-height: 1.05; letter-spacing: 1px;
  }
  .title-accent { font-size: 128px; margin-top: 6px; }
  .author-band {
    position: absolute; left: 0; right: 0; bottom: 0; height: 110px;
    background: linear-gradient(180deg, var(--gold-light) 0%, var(--gold) 50%, var(--gold-dark) 100%);
    display: flex; align-items: center; justify-content: center;
  }
  .author-band::before {
    content: ""; position: absolute; left: 0; right: 0; top: -14px; height: 4px;
    background: var(--gold);
  }
  .author-name {
    font-family: "Montserrat", sans-serif; font-weight: 800;
    color: var(--navy-deep); font-size: 36px; letter-spacing: 1.5px; text-transform: uppercase;
  }
</style>
</head>
<body>
<main class="canvas">
  <section class="book-cover">
    <div class="cover-photo" role="img" aria-label="Faint photo of a dental team treating a patient in a clinic"></div>

    <svg class="growth-graphic" viewBox="0 0 700 700" aria-hidden="true">
      <defs>
        <linearGradient id="arrow-gold" gradientUnits="userSpaceOnUse" x1="530" y1="275" x2="665" y2="90">
          <stop offset="0" stop-color="#a8801e"/>
          <stop offset=".5" stop-color="#f6e27a"/>
          <stop offset="1" stop-color="#d9b43c"/>
        </linearGradient>
      </defs>
      <g class="chart-bars" fill="rgba(160,200,240,.18)">
        <rect x="300" y="200" width="8" height="60"/>
        <rect x="318" y="180" width="8" height="80"/>
        <rect x="336" y="150" width="8" height="110"/>
        <rect x="354" y="170" width="8" height="90"/>
        <rect x="372" y="130" width="8" height="130"/>
        <rect x="390" y="150" width="8" height="110"/>
        <rect x="408" y="110" width="8" height="150"/>
        <rect x="426" y="125" width="8" height="135"/>
      </g>
      <g class="faint-arrows" fill="none" stroke="rgba(160,200,240,.35)" stroke-width="6">
        <polyline points="300,230 380,170 430,195 510,125"/>
        <polygon points="520,115 498,118 512,136" fill="rgba(160,200,240,.35)"/>
      </g>
      <g class="rising-arrow">
        <line x1="530" y1="275" x2="632" y2="135" stroke="url(#arrow-gold)" stroke-width="22"/>
        <polygon points="665,88 648,168 598,130" fill="url(#arrow-gold)"/>
      </g>
    </svg>

    <div class="title-block">
      <div class="title-lead">Build<br>Steady</div>
      <div class="title-divider"><span class="title-connector">Practice</span></div>
      <div class="title-main">Growth Through</div>
      <div class="title-accent">Trust</div>
    </div>

    <footer class="author-band">
      <span class="author-name">Daniel R. Porter, DDS</span>
    </footer>
  </section>
</main>
</body>
</html>
```